6 page (for now) squarespace website design for a Mobile Fitness small business

My sons California based small business "BrellaFit Coaching" with new subsidiary called "BrellaFit 4 Kids". I don't understand coding the website, is that the function squarespace provides?
In the end I want a working website, squarespace, I have a google workspace domain, email and subscription to squarespace & google workspace. URLs include brellafitcoaching.example and brellafit4kids.example. I have an idea of what I am looking for in a website and I have some examples of website designs I like, but I am 100% open to your design concepts and artistic flair. email is morgan@brellafitcoaching.example
I am looking for someone to design the site, help me understand how to make "minor" changes and hopefully have a long term relationship on the tech side of the business. I need an Idea of pricing for future changes (Rate T&M).
There are 2 businesses so I need a way to incorporate both the main company and a subsidiary into 1 website or link it somehow. I am open to your suggestions how to accomplish that. Do I need 2 completely separate websites or can it be done on 1 site directing you to different pages. I read conflicting info if it is a BAD idea to link 2 different websites so I will defer to your advice.
Below are the pages I need designed:
- Home Page- BrellaFit Coaching
- Home Page- BrellaFit 4 Kids (Homeschool market)
- Member Page (subscription service?)
- Workouts- with video clips 1-6 min each
- About
- Contact
- FAQ's
Future work & page designs:
- Store with training subscriptions & a few merch items
- Booking Appointments
- Bookshelf
- email campaign
-Blog
I like the feel of this website:
https://quillstride.example/

```html
<!DOCTYPE html>
<html lang="en">
<head>
<meta charset="utf-8">
<title>BrellaFit Coaching</title>
<link href="https://fonts.googleapis.com/css2?family=Montserrat:wght@400;500;600;700;800&display=swap" rel="stylesheet">
<style>
:root{
  --black:#0b0b0b;
  --ink:#141414;
  --white:#ffffff;
  --grey:#8a8a8a;
  --light:#f2f2f2;
  --red:#e8141b;
  --dark-band:#1c1c1c;
}
*{margin:0;padding:0;box-sizing:border-box}
html,body{width:1200px;height:4164px;overflow:hidden}
body{font-family:'Montserrat',Arial,sans-serif;color:var(--ink);background:var(--white);position:relative}
.abs{position:absolute}

/* hero */
.hero{position:absolute;left:0;top:0;width:1200px;height:720px;
  background:linear-gradient(100deg,#1d1f22 0%,#2e3033 40%,#4a4540 62%,#2b2623 80%,#151414 100%)}
.brand-box{position:absolute;left:0;top:0;width:420px;height:120px;background:var(--white);
  clip-path:polygon(0 0,100% 0,82% 100%,0 100%);display:flex;align-items:center;padding-left:120px;gap:14px}
.brand-dot{width:34px;height:34px;border-radius:50%;background:var(--ink)}
.brand-name{font-weight:700;font-size:26px;letter-spacing:3px;color:var(--ink)}
.main-nav{position:absolute;left:432px;top:54px;display:flex;gap:24px}
.main-nav a{color:var(--white);font-size:15px;font-weight:500;text-decoration:none;letter-spacing:.5px}
.hero-kicker{position:absolute;left:140px;top:290px;color:var(--white);font-size:32px;font-weight:700;letter-spacing:1px}
.hero-title{position:absolute;left:140px;top:330px;color:var(--white);font-size:76px;font-weight:800;letter-spacing:2px}
.btn-outline{position:absolute;border:3px solid var(--white);border-radius:40px;color:var(--white);
  font-weight:600;font-size:22px;display:flex;align-items:center;justify-content:center;letter-spacing:.5px}

/* section titles */
.section-title{position:absolute;left:0;width:1200px;display:flex;justify-content:center;align-items:center;gap:20px;
  font-size:52px;font-weight:800;letter-spacing:1px}
.title-dot{width:42px;height:42px;border-radius:50%;background:currentColor}

/* classes */
.class-item{position:absolute;width:300px;text-align:center}
.class-photo{width:256px;height:256px;border-radius:50%;margin:0 auto}
.class-name{margin-top:34px;font-size:26px;font-weight:700}
.class-text{margin-top:10px;font-size:16px;color:var(--grey);line-height:1.4}

/* bookshelf */
.bookshelf-band{position:absolute;left:0;top:1528px;width:1200px;height:540px;background:var(--black)}
.bookshelf-photo{position:absolute;left:172px;top:1448px;width:412px;height:620px;
  background:linear-gradient(160deg,#c8c2bb 0%,#8f8780 40%,#3c3a38 75%,#1e1d1c 100%)}
.body-copy{font-size:18px;line-height:1.5;color:var(--white)}

/* merch */
.merch-card{position:absolute;top:2252px;width:268px;height:376px;background:var(--white);
  box-shadow:0 4px 18px rgba(0,0,0,.14);text-align:center}
.merch-photo{width:100%;height:212px;background:var(--light);display:flex;align-items:center;justify-content:center}
.merch-name{margin-top:44px;font-size:20px;color:var(--grey)}
.merch-price{margin-top:12px;font-size:28px;font-weight:700}
.arrow-btn{position:absolute;top:2436px;width:52px;height:52px;border:2px solid var(--ink);border-radius:50%;
  display:flex;align-items:center;justify-content:center}

/* newsletter */
.newsletter{position:absolute;left:0;top:2752px;width:1200px;height:352px;
  background:linear-gradient(90deg,#121212,#2a2a2a 45%,#1f1f1f 70%,#0f0f0f)}
.email-field{position:absolute;left:288px;top:2980px;width:624px;height:56px;background:var(--white);border-radius:30px;overflow:hidden}
.email-field span{position:absolute;left:34px;top:20px;font-size:13px;color:var(--grey);letter-spacing:.5px}
.email-submit{position:absolute;right:0;top:0;width:166px;height:56px;background:var(--red);color:var(--white);
  font-weight:700;font-size:17px;display:flex;align-items:center;justify-content:center;border-radius:30px}

/* blog */
.blog-feature{position:absolute;left:172px;top:3276px;width:396px;height:432px;background:var(--red)}
.blog-feature .photo{height:184px;background:linear-gradient(135deg,#3a3a3a,#6d6864 50%,#2a2a2a)}
.blog-feature h3{margin:26px 0 0 26px;font-size:22px;font-weight:700;color:var(--white)}
.blog-feature p{margin:12px 26px 0;font-size:15px;line-height:1.4;color:var(--white)}
.blog-feature .date{margin:16px 26px 0;font-size:15px;font-weight:700;color:var(--white)}
.blog-photo{position:absolute;left:600px;width:216px;height:188px}
.blog-side{position:absolute;left:836px;width:230px}
.blog-side h3{font-size:22px;font-weight:700}
.blog-side p{margin-top:14px;font-size:15px;line-height:1.4}
.blog-side .date{margin-top:16px;font-size:15px;font-weight:700}

/* footer */
.footer{position:absolute;left:0;top:3780px;width:1200px;height:384px;background:var(--black);color:var(--white)}
.footer-brand{position:absolute;left:172px;top:70px;width:220px;text-align:center}
.footer-dot{width:100px;height:100px;border-radius:50%;background:var(--white);margin:0 auto}
.footer-name{margin-top:24px;font-size:34px;font-weight:600;letter-spacing:4px}
.social{display:flex;justify-content:center;gap:22px;margin-top:22px}
.social span{width:18px;height:18px;border-radius:50%;background:#7a7a7a}
.footer-col{position:absolute;top:76px}
.footer-col h4{font-size:18px;font-weight:700;letter-spacing:1px}
.footer-col ul{list-style:none;margin-top:22px}
.footer-col li{font-size:12px;color:#cfcfcf;margin-bottom:30px;letter-spacing:.5px}
.contact-row{display:flex;gap:18px;align-items:flex-start;margin-top:22px;font-size:14px;line-height:1.35}
.footer-rule{position:absolute;left:0;top:322px;width:1200px;height:1px;background:#333}
.copyright{position:absolute;left:0;top:342px;width:1200px;text-align:center;font-size:12px;color:#cfcfcf}
</style>
</head>
<body>

<header class="hero" role="img" aria-label="Athlete training with battle ropes in a gym">
  <div class="brand-box"><span class="brand-dot"></span><span class="brand-name">BRELLAFIT</span></div>
  <nav class="main-nav">
    <a href="#">HOME</a><a href="#">BRELLAFIT</a><a href="#">MEMBER</a><a href="#">WORKOUTS</a><a href="#">ABOUT</a><a href="#">CONTACT</a><a href="#">FAQS</a>
  </nav>
  <div class="hero-kicker">WELCOME TO</div>
  <h1 class="hero-title">BRELLAFIT</h1>
  <div class="btn-outline" style="left:140px;top:436px;width:324px;height:80px">BOOK APPOINTMENT</div>
</header>

<h2 class="section-title" style="top:786px"><span class="title-dot"></span>TRAINING CLASSES</h2>

<div class="class-item" style="left:158px;top:912px">
  <div class="class-photo" role="img" aria-label="Pilates exercise with a stability ball" style="background:linear-gradient(150deg,#d9d9d9,#8c8c8c 60%,#3a3a3a)"></div>
  <div class="class-name">PILATES</div>
  <div class="class-text">Lorem ipsum dolor sit amet<br>eiusmod consectetur<br>adipiscing elit</div>
</div>
<div class="class-item" style="left:458px;top:912px">
  <div class="class-photo" role="img" aria-label="Abdominal training session in a gym" style="background:linear-gradient(150deg,#6e6e6e,#3b3b3b 55%,#1b1b1b)"></div>
  <div class="class-name">ABS</div>
  <div class="class-text">Lorem ipsum dolor sit amet<br>eiusmod consectetur<br>adipiscing elit</div>
</div>
<div class="class-item" style="left:746px;top:912px">
  <div class="class-photo" role="img" aria-label="Cardio workout with a trainer" style="background:linear-gradient(150deg,#2a3a4d,#6a4b3c 55%,#1d1d1d)"></div>
  <div class="class-name">CARDIO</div>
  <div class="class-text">Lorem ipsum dolor sit amet<br>eiusmod consectetur<br>adipiscing elit</div>
</div>

<section>
  <div class="bookshelf-band"></div>
  <div class="bookshelf-photo" role="img" aria-label="Trainer coaching a client on a squat rack"></div>
  <h2 class="section-title" style="top:1604px;left:632px;width:auto;color:var(--white);font-size:48px;gap:16px"><span class="title-dot" style="width:38px;height:38px"></span>BOOKSHELF</h2>
  <p class="abs body-copy" style="left:632px;top:1684px;width:470px">Lorem ipsum dolor sit amet, consectetur adipiscing elit, sed do eiusmod tempor incididunt ut labore et dolore magna aliqua.Ut enim ad minim veniam, quis nostrud exercitation ullamco laboris nisi ut aliquip ex ea commodo consequat.Duis aute irure dolor in reprehenderit in a nulla pariatur.</p>
  <div class="btn-outline" style="left:632px;top:1936px;width:200px;height:62px;font-size:18px">READ MORE</div>
</section>

<h2 class="section-title" style="top:2138px"><span class="title-dot"></span>MERCH ITEMS</h2>
<div class="arrow-btn" style="left:56px"><svg width="20" height="20" viewBox="0 0 20 20"><path d="M13 3 L6 10 L13 17" fill="none" stroke="#141414" stroke-width="2.5"/></svg></div>
<div class="arrow-btn" style="left:1090px"><svg width="20" height="20" viewBox="0 0 20 20"><path d="M7 3 L14 10 L7 17" fill="none" stroke="#141414" stroke-width="2.5"/></svg></div>

<div class="merch-card" style="left:172px">
  <div class="merch-photo"><div role="img" aria-label="Black branded t-shirt" style="width:150px;height:170px;background:#111"></div></div>
  <div class="merch-name">Lorem Ipsum</div><div class="merch-price">$ 60.00</div>
</div>
<div class="merch-card" style="left:464px">
  <div class="merch-photo"><div role="img" aria-label="White branded t-shirt" style="width:150px;height:170px;background:#fafafa;border:1px solid #ddd"></div></div>
  <div class="merch-name">Lorem Ipsum</div><div class="merch-price">$ 79.00</div>
</div>
<div class="merch-card" style="left:756px">
  <div class="merch-photo"><div role="img" aria-label="Black branded tank top" style="width:130px;height:180px;background:#151515"></div></div>
  <div class="merch-name">Lorem Ipsum</div><div class="merch-price">$ 60.00</div>
</div>

<section class="newsletter" role="img" aria-label="Dimly lit gym interior"></section>
<h2 class="section-title" style="top:2788px;color:var(--white);font-size:50px">NEWSLETTER SUBSCRIPTION</h2>
<p class="abs body-copy" style="left:240px;top:2886px;width:720px;text-align:center;font-size:19px">Lorem ipsum dolor sit amet, sed do eiusmod tempor incididunt ut labore et dolore magna aliqua.</p>
<div class="email-field"><span>ENTER YOUR EMAIL</span><div class="email-submit">SUBSCRIBE</div></div>

<h2 class="section-title" style="top:3166px"><span class="title-dot"></span>BLOG</h2>
<article class="blog-feature">
  <div class="photo" role="img" aria-label="Group workout in a gym"></div>
  <h3>Blog Post</h3>
  <p>Lorem ipsum dolor sit amet, consectetur adipiscing elit, sed do eiusmod tempor incididunt ut labore et dolore magna aliqua.</p>
  <div class="date">26-01-2022</div>
</article>
<div class="blog-photo" role="img" aria-label="Trainer spotting a client" style="top:3276px;background:linear-gradient(135deg,#4a4a4a,#8a827b 50%,#2b2b2b)"></div>
<div class="blog-side" style="top:3290px"><h3>Blog Post</h3><p>Lorem ipsum dolor sit amet, consectetur adipiscing elit, sed do eiusmod tempor</p><div class="date">26-01-2022</div></div>
<div class="blog-photo" role="img" aria-label="Athlete lifting weights" style="top:3480px;background:linear-gradient(135deg,#2c2c2c,#6b625c 50%,#1d1d1d)"></div>
<div class="blog-side" style="top:3494px"><h3>Blog Post</h3><p>Lorem ipsum dolor sit amet, consectetur adipiscing elit, sed do eiusmod tempor</p><div class="date">26-01-2022</div></div>

<footer class="footer">
  <div class="footer-brand">
    <div class="footer-dot"></div>
    <div class="footer-name">BRELLAFIT</div>
    <div class="social"><span></span><span></span><span></span></div>
  </div>
  <div class="footer-col" style="left:456px"><h4>LINKS</h4><ul><li>HOME</li><li>CLASSES</li><li>REVIEWS</li><li>BLOG</li></ul></div>
  <div class="footer-col" style="left:620px"><h4>LEGAL</h4><ul><li>PRIVACY POLICY</li><li>TERMS &amp; CONDITIONS</li><li>CONTACT US</li><li>COOKIE POLICY</li></ul></div>
  <div class="footer-col" style="left:820px"><h4>CONTACT US</h4>
    <div class="contact-row"><svg width="18" height="24" viewBox="0 0 18 24"><path d="M9 1C4.6 1 1 4.5 1 9c0 6 8 14 8 14s8-8 8-14c0-4.5-3.6-8-8-8z" fill="#fff"/><circle cx="9" cy="9" r="3" fill="#0b0b0b"/></svg><span>Lorem ipsum dolor<br>sit amet, consectetur</span></div>
    <div class="contact-row"><svg width="20" height="20" viewBox="0 0 20 20"><path d="M4 1l4 4-2 3c1 2 4 5 6 6l3-2 4 4-3 3C8 19 1 12 1 4z" fill="#fff"/></svg><span>(555) 010-0199</span></div>
    <div class="contact-row"><svg width="22" height="16" viewBox="0 0 22 16"><rect x="1" y="1" width="20" height="14" fill="none" stroke="#fff" stroke-width="2"/><path d="M1 1l10 8 10-8" fill="none" stroke="#fff" stroke-width="2"/></svg><span>HELLO@BRELLAFIT.EXAMPLE</span></div>
  </div>
  <div class="footer-rule"></div>
  <div class="copyright">copyright 2022 BRELLAFIT . All rights reserved &nbsp;Terms &amp; Conditions</div>
</footer>

</body>
</html>
```